Event Website Design

We need a new website design for an events driven website. The domain for this site is http://brackenmoorhalls.co.uk. The site is up and running but needs a new fresh, modern look.
I've attached a Balamiq Mockup for the layout of the home page. Also attached is a png of the logo.
Key colours for the site are 0f7e6a, 35bde, d57835 & 373737.
Font to use is Proxima Nova
Width of the site should be 1200px
The design should be contemporary with minimal clutter.
Websites to references are…
http://vantorium.london/
http://www.thegpz.co.uk/
These are just guidelines, please feel free to use you own creative judgment.
The selected design file needs to be supplied as an editable PSD.
Reason: I've submitted 5 designs to the client, who will select the one they want. I will then choose that design. So please be patient as I'm waiting for a decision from my client.
Events
1 page

```html
<!DOCTYPE html>
<html lang="en">
<head>
<meta charset="utf-8">
<title>Brackenmoor Halmsworth – Home</title>
<link rel="stylesheet" href="https://fonts.googleapis.com/css2?family=Montserrat:wght@400;500;600;700&family=Raleway:wght@400;500;600&family=Cinzel:wght@400;600&display=swap">
<style>
:root{
  --teal:#0f7e6a;
  --blue:#135bde;
  --orange:#d57835;
  --charcoal:#373737;
  --ink:#2a2a2a;
  --text:#555;
  --white:#fff;
}
*{box-sizing:border-box;margin:0;padding:0}
html,body{width:1200px;height:2941px;overflow:hidden}
body{position:relative;font-family:"Montserrat",sans-serif;color:var(--text);background:var(--white)}
.abs{position:absolute}

/* top strip */
.topbar{left:0;top:0;width:1200px;height:28px;background:var(--orange);color:var(--white);font-size:10px;display:flex;align-items:center;padding:0 153px;justify-content:space-between;white-space:nowrap}
.topbar .box-office{font-weight:600;font-size:12px}
.topbar .links span{margin:0 4px}

/* header */
.header{left:0;top:28px;width:1200px;height:82px;background:var(--charcoal)}
.brand{left:153px;top:22px;display:flex;align-items:center;gap:10px;color:var(--white);font-weight:700;font-size:20px;letter-spacing:1px;white-space:nowrap}
.brand .mark{width:14px;height:14px;background:var(--teal)}
.search{left:765px;top:27px;width:286px;height:32px;border:1px solid #aaa;border-radius:16px;color:#999;font-size:11px;padding:0 16px;display:flex;align-items:center;justify-content:space-between}

/* nav */
.nav{left:0;top:110px;width:1200px;height:47px;display:flex;justify-content:center;align-items:center;font-size:13px;color:#333;white-space:nowrap}
.nav span.sep{margin:0 7px;color:#666}

/* hero */
.hero{left:0;top:157px;width:1200px;height:484px;background:
  radial-gradient(ellipse 180px 220px at 10% 45%,rgba(120,70,60,.75),transparent 70%),
  radial-gradient(ellipse 200px 240px at 38% 50%,rgba(230,180,150,.55),transparent 70%),
  radial-gradient(ellipse 220px 240px at 62% 40%,rgba(240,200,170,.6),transparent 70%),
  radial-gradient(ellipse 160px 200px at 90% 50%,rgba(160,100,90,.6),transparent 70%),
  radial-gradient(ellipse 300px 120px at 60% 95%,rgba(60,80,160,.6),transparent 70%),
  linear-gradient(180deg,#2a2250 0%,#4a2a4a 50%,#2a1a30 100%)}
.dots{left:0;top:611px;width:1200px;display:flex;justify-content:center;gap:10px}
.dots i{width:10px;height:10px;border-radius:50%;background:rgba(255,255,255,.6)}
.dots i:first-child{background:var(--white)}

/* events carousel */
.event{top:726px;width:230px;text-align:center}
.event .photo{width:153px;height:153px;border-radius:50%;margin:0 auto;border:3px solid #fff;box-shadow:0 0 0 1px #ddd}
.event h3{margin-top:33px;font-size:18px;font-weight:600;color:var(--blue);white-space:nowrap}
.event .rule{width:22px;height:3px;background:var(--teal);margin:9px auto 0}
.event .date{margin-top:12px;font-size:10px;color:#444}
.event .date b{color:var(--teal)}
.event .btns{margin-top:24px;display:flex;justify-content:center;gap:8px}
.btn{background:var(--blue);color:var(--white);font-size:12px;font-weight:600;border-radius:16px;width:74px;height:32px;display:flex;align-items:center;justify-content:center}
.arrow{top:872px;width:32px;height:32px;border:1px solid var(--teal);border-radius:50%;display:flex;align-items:center;justify-content:center}

/* features band */
.features{left:0;top:1137px;width:1200px;height:388px;background:
  radial-gradient(circle 60px at 20% 20%,rgba(255,230,180,.45),transparent 70%),
  radial-gradient(circle 50px at 85% 25%,rgba(255,220,200,.4),transparent 70%),
  radial-gradient(circle 70px at 60% 80%,rgba(200,120,150,.35),transparent 70%),
  linear-gradient(100deg,#c79a4a 0%,#9a6a5a 25%,#6a3a55 50%,#3a2340 70%,#6a3a50 100%)}
.feature{top:1220px;width:284px}
.feature .frame{height:196px;background:rgba(255,255,255,.55);padding:8px 8px 0;position:relative}
.feature .photo{height:180px}
.feature .more{position:absolute;left:8px;right:8px;bottom:0;height:38px;background:rgba(19,91,222,.85);color:var(--white);font-size:14px;font-weight:600;display:flex;align-items:center;justify-content:flex-end;padding-right:14px}
.feature h4{margin-top:20px;text-align:center;font-family:"Cinzel",serif;font-weight:600;font-size:17px;color:var(--white);white-space:nowrap}

/* news */
.news-head{left:0;top:1612px;width:1200px;text-align:center}
.news-head h2{font-family:"Cinzel",serif;font-weight:600;color:var(--orange);font-size:24px}
.news-head .rule{width:22px;height:3px;background:var(--blue);margin:14px auto 0}
.news-head a{display:block;margin-top:24px;font-size:15px;color:#444;text-decoration:none}
.card{top:1767px;width:292px;height:388px;border:1px solid #ddd;border-top:16px solid var(--orange);background:var(--white)}
.card .photo{height:170px}
.card h3{margin-top:18px;text-align:center;font-family:"Raleway",sans-serif;font-weight:600;font-size:20px;color:var(--orange)}
.card p{margin:14px 20px 0;text-align:center;font-size:12.5px;line-height:20px;color:#666}
.card .read{position:absolute;left:0;right:0;bottom:0;height:60px;background:var(--orange);color:var(--white);font-size:20px;display:flex;align-items:center;justify-content:center}

/* sports */
.sports{left:0;top:2255px;width:1200px;height:394px;background:
  radial-gradient(ellipse 420px 260px at 50% 55%,rgba(220,200,190,.35),transparent 70%),
  radial-gradient(ellipse 300px 200px at 15% 30%,rgba(120,150,80,.6),transparent 70%),
  radial-gradient(ellipse 300px 200px at 85% 30%,rgba(110,140,70,.6),transparent 70%),
  linear-gradient(180deg,#3f5a2e 0%,#2f4a26 55%,#6b7a5a 100%)}
.sports-caption{left:339px;top:2465px;width:520px;height:112px;background:rgba(0,0,0,.72);text-align:center;padding-top:18px}
.sports-caption h2{font-family:"Cinzel",serif;font-weight:600;color:var(--orange);font-size:32px}
.sports-caption p{margin-top:8px;color:var(--white);font-size:12px;font-weight:500}

/* footer */
.footer{left:0;top:2649px;width:1200px;height:224px;background:var(--charcoal)}
.footer ul{position:absolute;top:50px;list-style:none;color:var(--white);font-size:11px;white-space:nowrap}
.footer li{height:25.5px;display:flex;align-items:center;gap:8px}
.footer li::before{content:"";width:7px;height:7px;border-radius:50%;border:1.5px solid var(--blue);flex:none}
.footer .brand{left:836px;top:70px;font-size:28px}
.bottombar{left:0;top:2873px;width:1200px;height:68px;background:var(--ink);color:#ccc;font-size:10px}
.bottombar .copy{position:absolute;left:153px;top:28px}
.social{position:absolute;top:19px;width:31px;height:31px;border-radius:50%;background:var(--orange);display:flex;align-items:center;justify-content:center}
</style>
</head>
<body>

<div class="abs topbar">
  <span>Dunmere Vale's Premier Entertainment &amp; Sporting Centre</span>
  <span class="box-office">Box Office: 01632 960 482</span>
  <span class="links">Gift Voucher<span>|</span>Join Our Mailing List<span>|</span>My Account<span>|</span>Basket<span>|</span>Register</span>
</div>

<header class="abs header">
  <div class="abs brand"><span class="mark"></span>BRACKENMOOR</div>
  <div class="abs search">Search
    <svg width="14" height="14" viewBox="0 0 14 14"><circle cx="6" cy="6" r="4.5" fill="none" stroke="#fff" stroke-width="1.6"/><line x1="9.3" y1="9.3" x2="13" y2="13" stroke="#fff" stroke-width="1.6"/></svg>
  </div>
</header>

<nav class="abs nav">
  <span>What's On</span><span class="sep">/</span><span>Conferencing &amp; Events</span><span class="sep">/</span><span>Sports &amp; Leisure</span><span class="sep">/</span><span>Lantern Theatre</span><span class="sep">/</span><span>Plan Your Visit</span><span class="sep">/</span><span>News</span><span class="sep">/</span><span>Discover More</span><span class="sep">/</span><span>Contact Us</span>
</nav>

<section class="abs hero" role="img" aria-label="Guests celebrating with drinks at a party night"></section>
<div class="abs dots"><i></i><i></i><i></i></div>

<div class="abs arrow" style="left:86px"><svg width="12" height="12" viewBox="0 0 12 12"><path d="M8 2 L4 6 L8 10" fill="none" stroke="#333" stroke-width="1.5"/></svg></div>
<div class="abs arrow" style="left:1082px"><svg width="12" height="12" viewBox="0 0 12 12"><path d="M4 2 L8 6 L4 10" fill="none" stroke="#333" stroke-width="1.5"/></svg></div>

<article class="abs event" style="left:142px">
  <div class="photo" role="img" aria-label="Decorated dinner table setting" style="background:radial-gradient(circle at 40% 30%,#f0d8e0 0%,#d9b08a 45%,#8a6040 100%)"></div>
  <h3>NULLAM PRETIUM</h3><div class="rule"></div>
  <p class="date">Date : 04/01/2017 <b>( Monday )</b></p>
  <div class="btns"><span class="btn">MORE</span><span class="btn">BOOK</span></div>
</article>
<article class="abs event" style="left:371px">
  <div class="photo" role="img" aria-label="Speaker presenting at a conference" style="background:radial-gradient(circle at 50% 60%,#4a6ab0 0%,#a8c0d8 40%,#f2f4f6 80%)"></div>
  <h3>NULLAM PRETIUM</h3><div class="rule"></div>
  <p class="date">Date : 04/01/2017 <b>( Monday )</b></p>
  <div class="btns"><span class="btn">MORE</span><span class="btn">BOOK</span></div>
</article>
<article class="abs event" style="left:601px">
  <div class="photo" role="img" aria-label="Banquet hall lit in purple" style="background:radial-gradient(circle at 50% 35%,#f0e0ff 0%,#b070e0 35%,#5a2a9a 75%,#2a1050 100%)"></div>
  <h3>NULLAM PRETIUM</h3><div class="rule"></div>
  <p class="date">Date : 04/01/2017 <b>( Monday )</b></p>
  <div class="btns"><span class="btn">MORE</span><span class="btn">BOOK</span></div>
</article>
<article class="abs event" style="left:830px">
  <div class="photo" role="img" aria-label="Crowd relaxing on a lawn at an outdoor event" style="background:linear-gradient(180deg,#b8d0e8 0%,#6a8a50 35%,#5a5060 60%,#4a8a30 100%)"></div>
  <h3>NULLAM PRETIUM</h3><div class="rule"></div>
  <p class="date">Date : 04/01/2017 <b>( Monday )</b></p>
  <div class="btns"><span class="btn">MORE</span><span class="btn">BOOK</span></div>
</article>

<section class="abs features" role="img" aria-label="Blurred party lights background"></section>
<div class="abs feature" style="left:153px">
  <div class="frame"><div class="photo" role="img" aria-label="Presenter addressing a conference audience" style="background:linear-gradient(180deg,#eef0f2 0%,#c8ccd0 40%,#5a5e66 100%)"></div><div class="more">KNOW MORE</div></div>
  <h4>CONFERENCES &amp; EVENTS</h4>
</div>
<div class="abs feature" style="left:457px">
  <div class="frame"><div class="photo" role="img" aria-label="Friends in festive hats toasting at a party" style="background:radial-gradient(ellipse at 50% 40%,#f0c8a0 0%,#c07858 45%,#6a2a20 100%)"></div><div class="more">KNOW MORE</div></div>
  <h4>PARTIES AT BRACKENMOOR</h4>
</div>
<div class="abs feature" style="left:763px">
  <div class="frame"><div class="photo" role="img" aria-label="People working on laptops in a shared workspace" style="background:linear-gradient(180deg,#f2f0ec 0%,#b8a898 45%,#3a302a 100%)"></div><div class="more">KNOW MORE</div></div>
  <h4>CO-WORKING HUB</h4>
</div>

<div class="abs news-head">
  <h2>LATEST FROM BRACKENMOOR</h2>
  <div class="rule"></div>
  <a href="#">See All News</a>
</div>
<article class="abs card" style="left:151px">
  <div class="photo" role="img" aria-label="Guests raising glasses at a reception" style="background:linear-gradient(180deg,#f4f2ee 0%,#d8cfc2 50%,#8a7a68 100%)"></div>
  <h3>MAURIS LAOREET</h3>
  <p>Integer malesuada mi metus, non dolor condimentum sed. Vivamus ullamcorper sagittis posuere. massa.</p>
  <div class="read">READ MORE</div>
</article>
<article class="abs card" style="left:455px">
  <div class="photo" role="img" aria-label="Crowd watching fireworks at night" style="background:radial-gradient(ellipse at 50% 20%,#8aa8d8 0%,#2a3a6a 45%,#0c1020 100%)"></div>
  <h3>MAURIS LAOREET</h3>
  <p>Integer malesuada mi metus, non dolor condimentum sed. Vivamus ullamcorper sagittis posuere. massa.</p>
  <div class="read">READ MORE</div>
</article>
<article class="abs card" style="left:761px">
  <div class="photo" role="img" aria-label="Festival crowd in warm sunlight" style="background:radial-gradient(ellipse at 30% 10%,#fff0c0 0%,#f0a050 35%,#a05a40 70%,#4a2a30 100%)"></div>
  <h3>MAURIS LAOREET</h3>
  <p>Integer malesuada mi metus, non dolor condimentum sed. Vivamus ullamcorper sagittis posuere. massa.</p>
  <div class="read">READ MORE</div>
</article>

<section class="abs sports" role="img" aria-label="Group of runners jogging through a park"></section>
<div class="abs sports-caption">
  <h2>SPORTS &amp; LEISURE</h2>
  <p>INTEGER ALIQUAM IN LIBERO QUIS</p>
</div>

<footer class="abs footer">
  <ul style="left:153px"><li>Brackenmoor Entertainment Venue</li><li>Fernleigh Close</li><li>Halmsworth</li><li>Dunmere Vale</li><li>HM4 7QX</li></ul>
  <ul style="left:390px"><li>What's On</li><li>Conferencing &amp; Events</li><li>Sports &amp; Leisure</li><li>Lantern Theatre</li></ul>
  <ul style="left:608px"><li>Plan Your Visit</li><li>News</li><li>Discover More</li><li>Contact Us</li></ul>
  <div class="abs brand"><span class="mark"></span>BRACKENMOOR</div>
</footer>

<div class="abs bottombar">
  <span class="copy">© 2017 Brackenmoor Halmsworth All Rights Reserved</span>
  <span class="social" style="left:922px" aria-label="Social link"></span>
  <span class="social" style="left:969px" aria-label="Social link"></span>
  <span class="social" style="left:1016px" aria-label="Basket">
    <svg width="16" height="16" viewBox="0 0 16 16"><path d="M1 2 H3.5 L5.5 11 H13 L14.5 5 H4.5" fill="none" stroke="#2a2a2a" stroke-width="1.6"/><circle cx="6.5" cy="13.5" r="1.2" fill="#2a2a2a"/><circle cx="12" cy="13.5" r="1.2" fill="#2a2a2a"/></svg>
  </span>
</div>

</body>
</html>
```